tax advisory service business cards
Professional
Loretta Fenwick
Tax Advisory Specialist
51924 HOLLISTER LANE SUITE C
CEDARMONT, TX 70812
FISCAL9COUNSELDESK@QUILLMAIL.COM
FCD4FILE.COM

```html
<!DOCTYPE html>
<html lang="en">
<head>
<meta charset="utf-8">
<title>Fiscal Counsel Desk – Business Cards</title>
<link rel="stylesheet" href="https://fonts.googleapis.com/css2?family=Tinos:ital,wght@0,400;0,700;1,400;1,700&display=swap">
<style>
  :root {
    --page-bg: #ecebe8;
    --navy: #1b2353;
    --navy-text: #1f2a5c;
    --gold: #c9a33a;
    --card-white: #ffffff;
  }
  * { margin: 0; padding: 0; box-sizing: border-box; }
  html, body {
    width: 1200px; height: 871px; overflow: hidden;
    background: var(--page-bg);
    font-family: "Tinos", "Times New Roman", serif;
  }
  .sheet {
    width: 1200px; height: 871px;
    display: flex; flex-direction: column;
    align-items: center; justify-content: center; gap: 56px;
  }
  .card {
    width: 620px; height: 354px;
    box-shadow: 0 6px 18px rgba(0,0,0,0.18);
    position: relative;
  }
  .card--back {
    background: var(--navy);
    display: flex; align-items: center; justify-content: center;
  }
  .back-mark {
    width: 132px; height: 132px; border-radius: 50%;
    background: var(--gold);
  }
  .card--front {
    background: var(--card-white);
    display: flex; align-items: center;
    padding: 0 40px 0 36px;
  }
  .brand {
    width: 290px;
    display: flex; flex-direction: column; align-items: center;
  }
  .brand-mark {
    width: 58px; height: 58px; border-radius: 50%;
    background: var(--navy);
    margin-bottom: 12px;
  }
  .brand-name {
    color: var(--navy-text);
    font-size: 19px; letter-spacing: 0.3px;
    text-transform: uppercase; white-space: nowrap;
  }
  .brand-tagline {
    margin-top: 4px; padding-top: 3px;
    border-top: 1px solid var(--navy-text);
    color: var(--navy-text);
    font-size: 9.5px; font-style: italic; white-space: nowrap;
  }
  .contact {
    margin-left: 30px;
    color: var(--navy-text);
    font-size: 10.5px; line-height: 1.45;
  }
  .contact-name { font-weight: 700; font-style: italic; font-size: 12.5px; }
  .contact-title { font-style: italic; margin-bottom: 14px; }
  .contact-address { margin-bottom: 12px; text-transform: uppercase; }
  .contact-line { display: flex; align-items: center; gap: 5px; text-transform: uppercase; }
  .contact-line svg { width: 9px; height: 9px; fill: var(--navy-text); flex: none; }
</style>
</head>
<body>
<main class="sheet">
  <section class="card card--back">
    <div class="back-mark"></div>
  </section>

  <section class="card card--front">
    <div class="brand">
      <div class="brand-mark"></div>
      <div class="brand-name">Fiscal Counsel Desk, Inc.</div>
      <div class="brand-tagline">Careful Counsel For Every Single Return</div>
    </div>
    <div class="contact">
      <div class="contact-name">Loretta Fenwick</div>
      <div class="contact-title">Tax Advisory Specialist</div>
      <div class="contact-address">51924 Hollister Lane Suite C<br>Cedarmont, TX 70812</div>
      <div class="contact-line">
        <svg viewBox="0 0 10 10"><path d="M2 0.5 L3.6 0.5 L4.3 2.8 L3.2 3.8 Q4.2 5.8 6.2 6.8 L7.2 5.7 L9.5 6.4 L9.5 8 Q9.5 9.5 8 9.5 Q1 9 0.5 2 Q0.5 0.5 2 0.5Z"/></svg>
        225-555-0148
      </div>
      <div class="contact-line">
        <svg viewBox="0 0 10 10"><rect x="0.5" y="2" width="9" height="6.5"/><path d="M0.5 2 L5 5.5 L9.5 2" stroke="#fff" stroke-width="0.8" fill="none"/></svg>
        fiscal9counseldesk@quillmail.com
      </div>
      <div class="contact-line">
        <svg viewBox="0 0 10 10"><circle cx="5" cy="5" r="4.3" fill="none" stroke="#1f2a5c" stroke-width="1"/><path d="M0.7 5 H9.3 M5 0.7 Q2.5 5 5 9.3 M5 0.7 Q7.5 5 5 9.3" stroke="#1f2a5c" stroke-width="0.7" fill="none"/></svg>
        www.fcd4file.com
      </div>
    </div>
  </section>
</main>
</body>
</html>
```